Amber Kettle Corp Business Card Design

Amber Kettle Corp is a local owner and operator of several coffee shops in Irving, TX. Google "Bean Harbor Plaza" for an example of one of our shops.We would like an image that is professional, but with a slight nod to the protestant religious nature of our backers.The name "Amber Kettle" is a play on the concept of "rivers of living water". It also conveys the concept of a "life of coffee". We desire to combine these concepts in the logo visualization, with the emphasis on the commercial side of the concept.

Target Market(s)

Upper class retail. No drive-through. Comfy lounges.

Industry/Entity Type

Coffee Shop

Contact Information for Business Card

Dale Fenwick
Chief Operating Officer
Amber Kettle Corp
(555) 417 2906
dale@amberkettle.example (address not yet active)

Requirements
Must have
• We do not have a logo yet. Need that as a part of the design.
• This needs to be original artwork. I need to own the art when the design is finished. I will look at submissions with stock artwork, but be advised that I will not accept the submission until original work is presented.

```html
<!DOCTYPE html>
<html lang="en">
<head>
<meta charset="utf-8">
<title>Amber Kettle Corp — Business Card</title>
<link rel="stylesheet" href="https://fonts.googleapis.com/css2?family=Arimo:wght@400;700&display=swap">
<style>
  :root {
    --card-bg: #ffffff;
    --ink: #3e5a4d;
    --accent-yellow: #f2f763;
  }
  html, body {
    margin: 0;
    padding: 0;
    width: 1200px;
    height: 702px;
    overflow: hidden;
    background: var(--card-bg);
  }
  .card {
    position: relative;
    width: 1200px;
    height: 702px;
    background: var(--card-bg);
    font-family: "Arimo", Arial, sans-serif;
    color: var(--ink);
  }
  .brand {
    position: absolute;
    left: 454px;
    top: 79px;
    width: 270px;
    height: 270px;
    display: flex;
    align-items: center;
    justify-content: center;
  }
  .brand-dot {
    position: absolute;
    inset: 0;
    width: 270px;
    height: 270px;
  }
  .brand-name {
    position: relative;
    font-size: 34px;
    font-weight: 400;
    color: var(--ink);
    letter-spacing: 0.5px;
    white-space: nowrap;
  }
  .contact {
    position: absolute;
    left: 0;
    top: 396px;
    width: 1200px;
    text-align: center;
    text-transform: uppercase;
  }
  .contact p {
    margin: 0;
    line-height: 56px;
    white-space: nowrap;
  }
  .contact-name {
    font-size: 44px;
    font-weight: 700;
    letter-spacing: 1px;
  }
  .contact-title,
  .contact-company {
    font-size: 48px;
    font-weight: 400;
    letter-spacing: 0.5px;
  }
  .contact-phone {
    font-size: 44px;
    font-weight: 400;
    letter-spacing: 3px;
  }
</style>
</head>
<body>
  <main class="card">
    <div class="brand">
      <svg class="brand-dot" viewBox="0 0 270 270" aria-hidden="true">
        <circle cx="135" cy="135" r="135" fill="var(--accent-yellow)"/>
      </svg>
      <span class="brand-name">Amber Kettle</span>
    </div>
    <section class="contact">
      <p class="contact-name">Dale Fenwick</p>
      <p class="contact-title">Chief Operating Officer</p>
      <p class="contact-company">Amber Kettle Corp</p>
      <p class="contact-phone">(555) 417 2906</p>
    </section>
  </main>
</body>
</html>
```